Business Cards for a small business advisory (business services)

Professional look. Same as would apply for a lawyer, accountant, or other financial services professional. Please use the logo colors

Target Market(s)

small business owners

Industry/Entity Type

Financial Servics

Contact Information for Business Card

Name: Gavin L. Whitmore, CAIA / Title: Business Advisor / Office #: (718) 294-7716 / Mobile #: (917) 382-5047 / Email: g.whitmore@clearfieldventurepartners.example / Web: www.clearfieldventurepartners.example

Font styles to use
Sans Serif

```html
<!DOCTYPE html>
<html lang="en">
<head>
<meta charset="utf-8">
<title>Clearfield Venture Partners – Business Cards</title>
<link rel="stylesheet" href="https://fonts.googleapis.com/css2?family=Montserrat:wght@500;600;700&family=Arimo:wght@400;700&display=swap">
<style>
  :root {
    --navy: #1b3a6b;
    --navy-deep: #163260;
    --navy-soft: #2a4c82;
    --green: #7dc242;
    --white: #ffffff;
    --backdrop: #e9e9e8;
    --brand-font: "Montserrat", sans-serif;
    --body-font: "Arimo", sans-serif;
  }
  * { box-sizing: border-box; margin: 0; padding: 0; }
  html, body { width: 1200px; height: 801px; overflow: hidden; }
  body {
    background: var(--backdrop);
    position: relative;
    font-family: var(--body-font);
  }
  .card {
    position: absolute;
    top: 240px;
    width: 540px;
    height: 309px;
    background: radial-gradient(ellipse at 40% 40%, #1f4178 0%, var(--navy) 55%, var(--navy-deep) 100%);
    border-bottom: 5px solid var(--green);
    overflow: hidden;
    color: var(--white);
  }
  .card--front { left: 40px; }
  .card--back { left: 620px; }

  .mark-field {
    position: absolute;
    border-radius: 50%;
    background: radial-gradient(circle, rgba(74,112,176,0.45) 0%, rgba(42,76,130,0.25) 55%, rgba(27,58,107,0) 72%);
  }
  .card--front .mark-field { right: -30px; top: -40px; width: 260px; height: 260px; }
  .card--back .mark-field { left: -30px; top: 90px; width: 280px; height: 280px; }

  .brand { position: absolute; display: flex; align-items: center; gap: 10px; }
  .brand__dot {
    width: 26px; height: 26px; border-radius: 50%;
    background: var(--white);
    flex: none;
  }
  .brand__name {
    font-family: var(--brand-font);
    font-weight: 700;
    color: var(--white);
    letter-spacing: 0.5px;
    line-height: 1;
  }
  .brand__tagline {
    position: absolute;
    font-family: var(--brand-font);
    font-weight: 600;
    text-transform: uppercase;
    color: var(--white);
    letter-spacing: 0.4px;
    white-space: nowrap;
  }

  .card--front .brand { left: 30px; top: 36px; }
  .card--front .brand__name { font-size: 44px; }
  .card--front .brand__tagline { left: 66px; top: 86px; font-size: 7px; }

  .card--back .brand { right: 34px; top: 196px; }
  .card--back .brand__dot { width: 30px; height: 30px; }
  .card--back .brand__name { font-size: 54px; }
  .card--back .brand__tagline { right: 34px; top: 256px; font-size: 8px; }

  .person { position: absolute; left: 66px; top: 122px; }
  .person__name {
    font-family: var(--brand-font);
    font-weight: 700;
    font-size: 24px;
    color: var(--green);
  }
  .person__title { font-size: 15px; margin-top: 4px; }

  .edge-tab {
    position: absolute;
    left: 0; top: 182px;
    width: 34px; height: 22px;
    background: var(--green);
  }

  .contacts {
    position: absolute;
    left: 66px; top: 196px;
    list-style: none;
  }
  .contacts li {
    display: flex; align-items: center; gap: 9px;
    font-size: 13.5px;
    line-height: 20px;
  }
  .contacts svg { width: 13px; height: 13px; flex: none; }
  .contacts svg * { stroke: var(--green); fill: none; stroke-width: 1.6; }
</style>
</head>
<body>

<section class="card card--front" aria-label="Business card front">
  <div class="mark-field" role="img" aria-label="Faint large brand mark decoration"></div>

  <div class="brand">
    <span class="brand__dot"></span>
    <span class="brand__name">Clearfield</span>
  </div>
  <p class="brand__tagline">Steady counsel to grow, fund or hand on your small business</p>

  <div class="person">
    <p class="person__name">Gavin L. Whitmore, CAIA</p>
    <p class="person__title">Business Advisor</p>
  </div>

  <span class="edge-tab"></span>

  <ul class="contacts">
    <li>
      <svg viewBox="0 0 14 14"><path d="M3 1.5l2 2.5-1.2 1.4c.8 1.7 2 2.9 3.8 3.8L9 8l2.5 2-1 2.5C6 12.5 1.5 8 1.5 3.5z"/></svg>
      (718) 294-7716
    </li>
    <li>
      <svg viewBox="0 0 14 14"><rect x="3.5" y="1" width="7" height="12" rx="1.3"/><line x1="6" y1="11" x2="8" y2="11"/></svg>
      (917) 382-5047
    </li>
    <li>
      <svg viewBox="0 0 14 14"><rect x="1" y="3" width="12" height="8.5" rx="1"/><path d="M1.5 3.5L7 8l5.5-4.5"/></svg>
      g.whitmore@clearfieldventurepartners.example
    </li>
    <li>
      <svg viewBox="0 0 14 14"><circle cx="7" cy="7" r="5.7"/><ellipse cx="7" cy="7" rx="2.4" ry="5.7"/><line x1="1.3" y1="7" x2="12.7" y2="7"/></svg>
      www.clearfieldventurepartners.example
    </li>
  </ul>
</section>

<section class="card card--back" aria-label="Business card back">
  <div class="mark-field" role="img" aria-label="Large embossed brand mark decoration"></div>

  <div class="brand">
    <span class="brand__dot"></span>
    <span class="brand__name">Clearfield</span>
  </div>
  <p class="brand__tagline">Steady counsel to grow, fund or hand on your small business</p>
</section>

</body>
</html>
```